Biz Card & Stationary for Business Coaching Co.
Plan. Act. Grow.
Biz Card & Stationary for Business Coaching Co. - Consulting
Creative Brief
Simple
Marlow Quint
CEO
2864 38th Ave S Minneapolis, MN 55406
marlow@brightharbor.net
www.brightharbor.net
My office is home based so we don't need to use the physical address on the card.
I would like to use my logo or at least the logo symbol somehow on the back. Perhaps incorporate tag line "Plan. Act. Grow."

```html
<!DOCTYPE html>
<html lang="en">
<head>
<meta charset="utf-8">
<title>Bright Harbor – Business Cards</title>
<link href="https://fonts.googleapis.com/css2?family=Montserrat:wght@500;700;800&family=Open+Sans:wght@400;600&display=swap" rel="stylesheet">
<style>
  :root{
    --bg:#6e7072;
    --blue-deep:#17307a;
    --blue-mid:#2446a8;
    --blue-light:#4d78d6;
    --grey-band:#9aa0aa;
    --white:#ffffff;
    --ink:#2a2f3a;
  }
  *{margin:0;padding:0;box-sizing:border-box}
  html,body{width:1200px;height:908px;overflow:hidden}
  body{background:var(--bg);font-family:"Open Sans",sans-serif;position:relative}
  .card{position:absolute;left:250px;width:700px;height:400px;border-radius:26px;overflow:hidden;box-shadow:0 10px 30px rgba(0,0,0,.35)}
  .card--front{top:34px;background:linear-gradient(135deg,var(--blue-light) 0%,var(--blue-mid) 45%,var(--blue-deep) 100%)}
  .card--back{top:474px;background:var(--white)}
  .brand{font-family:"Montserrat",sans-serif;font-weight:800;letter-spacing:2px;text-transform:uppercase}
  .front-brand{position:absolute;left:44px;bottom:56px;color:var(--white)}
  .front-brand .brand{font-size:38px;line-height:1}
  .descriptor{font-family:"Montserrat",sans-serif;font-weight:500;font-size:12px;letter-spacing:3px;text-transform:uppercase;margin-top:8px}
  .motto{font-family:"Montserrat",sans-serif;font-weight:700;font-size:15px;letter-spacing:2px;margin-top:22px;color:rgba(255,255,255,.85)}
  .back-art{position:absolute;inset:0}
  .back-person{position:absolute;right:44px;top:96px;text-align:right;color:var(--blue-mid)}
  .back-person .name{font-family:"Montserrat",sans-serif;font-weight:700;font-size:22px}
  .back-person .role{font-size:13px;font-weight:600;color:var(--ink);margin-top:2px}
  .back-logo{position:absolute;left:40px;top:232px;display:flex;align-items:center;gap:10px;color:var(--blue-deep)}
  .back-logo .dot{width:26px;height:26px;border-radius:50%;background:var(--blue-mid)}
  .back-logo .brand{font-size:22px}
  .contact{position:absolute;left:40px;top:290px;list-style:none;font-size:12.5px;color:var(--ink)}
  .contact li{display:flex;align-items:center;gap:8px;height:24px}
  .contact svg{width:15px;height:15px;flex:none}
</style>
</head>
<body>
  <section class="card card--front">
    <div class="front-brand">
      <div class="brand">Bright Harbor</div>
      <div class="descriptor">Business Coaching and Consulting</div>
      <div class="motto">Plan. Act. Grow.</div>
    </div>
  </section>

  <section class="card card--back">
    <svg class="back-art" viewBox="0 0 700 400" preserveAspectRatio="none">
      <defs>
        <linearGradient id="band" x1="0" y1="0" x2="1" y2="1">
          <stop offset="0" stop-color="#4d78d6"/>
          <stop offset=".5" stop-color="#2446a8"/>
          <stop offset="1" stop-color="#17307a"/>
        </linearGradient>
      </defs>
      <path d="M0,0 H700 V58 C520,88 260,150 0,228 Z" fill="url(#band)"/>
      <path d="M0,228 C260,150 520,88 700,58 V70 C520,100 260,165 0,250 Z" fill="#9aa0aa"/>
    </svg>
    <div class="back-person">
      <div class="name">Marlow Quint</div>
      <div class="role">CEO</div>
    </div>
    <div class="back-logo">
      <span class="dot"></span>
      <span class="brand">Bright Harbor</span>
    </div>
    <ul class="contact">
      <li><svg viewBox="0 0 16 16"><circle cx="8" cy="8" r="8" fill="#2446a8"/><path d="M5.5 4.5l1.5 1.5-1 1c.6 1.2 1.5 2.1 2.7 2.7l1-1 1.5 1.5-1 1.2c-2.7-.5-4.7-2.5-5.2-5.2z" fill="#fff"/></svg>612.555.0148</li>
      <li><svg viewBox="0 0 16 16"><circle cx="8" cy="8" r="8" fill="#2446a8"/><rect x="4" y="5" width="8" height="6" fill="none" stroke="#fff"/><path d="M4 5l4 3.5L12 5" fill="none" stroke="#fff"/></svg>marlow@brightharbor.net</li>
      <li><svg viewBox="0 0 16 16"><circle cx="8" cy="8" r="8" fill="#2446a8"/><circle cx="8" cy="8" r="4" fill="none" stroke="#fff"/><path d="M4 8h8M8 4v8" stroke="#fff"/></svg>www.brightharbor.net</li>
    </ul>
  </section>
</body>
</html>
```